Restaurant service company needs a website!

I am looking for a skilled web designer/developer to create a professional, responsive, and easy-to-navigate website for my company, which specializes in servicing restaurant cooking equipment. The site should communicate trust, reliability, and technical expertise to our target audience, restaurant owners, managers, and commercial kitchen operators. I have included the company logos, if any other format for them is needed please let me know.

Target Market(s)

restaurant owners, managers, and commercial kitchen operators

Industry/Entity Type

Commercial Kitchen Equipment Service

Coding

Coded - Design and coding required

Number of Pages Required

1 page

Font styles to use
Serif
Sans Serif

Requirements
Must have
• Contact and service request forms, Click-to-call functionality for mobile, Clean, modern layout with strong visuals, Easy navigation, mobile-friendly
Nice to have
• Testimonials or Reviews, If possible a click-to-text functionality for mobile.
Should not have
• Any mention of Refrigeration or HVAC, "Free Quotes"

```html
<!DOCTYPE html>
<html lang="en">
<head>
<meta charset="utf-8">
<title>Junction Kitchen Service</title>
<link href="https://fonts.googleapis.com/css2?family=Roboto:ital,wght@0,400;0,500;0,700;0,900;1,400&display=swap" rel="stylesheet">
<style>
:root{
  --teal:#0b6a80;
  --teal-deep:#085a6d;
  --teal-bright:#0a93b6;
  --ink:#111;
  --muted:#555;
  --white:#fff;
  --footer:#0b0b0b;
  --star:#f7931e;
}
*{box-sizing:border-box;margin:0;padding:0}
html,body{width:1200px;height:3666px;overflow:hidden}
body{font-family:"Roboto",sans-serif;color:var(--ink);background:var(--white);position:relative}
.abs{position:absolute}

/* header */
.site-header{position:absolute;left:0;top:0;width:1200px;height:88px;background:var(--white)}
.brand{position:absolute;left:112px;top:24px;display:flex;align-items:center;gap:10px;color:var(--teal);font-weight:700;font-size:26px;letter-spacing:.5px}
.brand-square{width:26px;height:26px;border:3px solid var(--teal)}
.main-nav{position:absolute;left:410px;top:33px;display:flex;gap:33px;font-size:17px;font-weight:500}
.main-nav a{color:var(--ink);text-decoration:none}
.main-nav a.active{color:var(--teal)}
.call-btn{position:absolute;left:940px;top:18px;width:147px;height:50px;background:var(--teal);border-radius:5px;color:var(--white);display:flex;align-items:center;justify-content:center;gap:12px;font-weight:700;font-size:17px;text-decoration:none}
.call-icon{width:32px;height:32px;border-radius:50%;background:var(--white);display:flex;align-items:center;justify-content:center}

/* hero */
.hero{position:absolute;left:0;top:88px;width:1200px;height:558px;background:linear-gradient(135deg,#3b3f44,#5a5f64 45%,#2c3034);text-align:center;color:var(--white)}
.hero-shade{position:absolute;inset:0;background:rgba(0,0,0,.35)}
.hero h1{position:absolute;left:0;right:0;top:255px;font-size:44px;font-weight:900;letter-spacing:.5px}
.hero p{position:absolute;left:0;right:0;top:324px;font-size:15.5px;line-height:30px}
.hero-btn{position:absolute;left:501px;top:402px;width:197px;height:50px;background:var(--teal);border-radius:4px;font-weight:700;font-size:17px;display:flex;align-items:center;justify-content:center}
.hero-arrow{position:absolute;top:262px}

/* section headings */
.section-title{position:absolute;left:0;right:0;text-align:center}
.section-title h2{font-size:38px;font-weight:900;color:var(--teal);letter-spacing:.5px}
.section-title p{font-style:italic;font-size:16.5px;color:#444;margin-top:14px}
.section-title.light h2,.section-title.light p{color:var(--white)}

/* services */
.service-card{position:absolute;top:878px;width:237px;height:225px;border-radius:12px}
.service-label{position:absolute;top:1070px;width:191px;height:65px;background:var(--white);border-radius:5px;box-shadow:0 2px 8px rgba(0,0,0,.15);display:flex;align-items:center;justify-content:center;text-align:center;font-weight:700;font-size:17px;line-height:22px}
.service-label.active{background:var(--teal);color:var(--white)}

/* about */
.about{position:absolute;left:0;top:1229px;width:1200px;height:581px;background:var(--teal)}
.about-text{position:absolute;left:660px;top:60px;width:430px;color:var(--white)}
.about-text h2{font-size:38px;font-weight:900}
.about-text .tag{font-style:italic;font-size:16.5px;margin-top:14px}
.about-text p.body{font-size:16.5px;line-height:30px;margin-top:26px}
.outline-btn{position:absolute;width:196px;height:51px;border:2px solid var(--white);border-radius:5px;color:var(--white);font-weight:700;font-size:17px;display:flex;align-items:center;justify-content:center}

/* testimonials */
.review{position:absolute;top:2064px;width:314px;height:351px;background:var(--white);box-shadow:0 2px 12px rgba(0,0,0,.12);padding:20px 18px}
.review p{font-style:italic;font-size:15px;line-height:30px;color:var(--muted)}
.reviewer{display:flex;align-items:center;gap:14px;margin-top:16px}
.avatar{width:58px;height:58px;border-radius:50%;border:3px solid var(--teal);background:linear-gradient(#b8d4e0,#7fa3b4)}
.reviewer h4{font-size:16px;font-weight:500}
.stars{color:var(--star);font-size:20px;letter-spacing:4px}

/* contact */
.contact{position:absolute;left:0;top:2505px;width:1200px;height:702px;background:linear-gradient(180deg,#0d6e86,#0b6279 60%,#0a5970)}
.field{position:absolute;background:var(--white);border-radius:5px;font-size:15.5px;font-weight:500;padding:18px 17px;color:#222}

/* footer */
.site-footer{position:absolute;left:0;top:3207px;width:1200px;height:459px;background:var(--footer);color:var(--white)}
.footer-brand{position:absolute;left:112px;top:160px;display:flex;align-items:center;gap:12px;color:var(--teal-bright);font-weight:700;font-size:32px}
.footer-brand .brand-square{width:34px;height:34px;border-color:var(--teal-bright)}
.footer-col h3{font-size:19px;font-weight:700;letter-spacing:.3px}
.footer-col ul{list-style:none;margin-top:30px}
.footer-col li{font-size:15.5px;margin-bottom:19px}
.contact-line{display:flex;gap:10px;font-size:15.5px;line-height:21px}
.footer-rule{position:absolute;left:112px;top:366px;width:976px;height:1px;background:#333}
.copyright{position:absolute;left:0;right:0;top:401px;text-align:center;font-size:15.5px}
</style>
</head>
<body>

<header class="site-header">
  <div class="brand"><span class="brand-square"></span>JUNCTION</div>
  <nav class="main-nav">
    <a class="active" href="#">HOME</a><a href="#">ABOUT US</a><a href="#">OUR SERVICE</a><a href="#">WHY CHOOSE US</a>
  </nav>
  <a class="call-btn" href="tel:+15550142760">
    <span class="call-icon"><svg width="18" height="18" viewBox="0 0 24 24"><path fill="#0b6a80" d="M6.6 10.8a15 15 0 0 0 6.6 6.6l2.2-2.2c.3-.3.7-.4 1-.2 1.1.4 2.3.6 3.6.6.6 0 1 .4 1 1V20c0 .6-.4 1-1 1A17 17 0 0 1 3 4c0-.6.4-1 1-1h3.5c.6 0 1 .4 1 1 0 1.3.2 2.5.6 3.6.1.3 0 .7-.2 1z"/></svg></span>
    Call Now
  </a>
</header>

<section class="hero">
  <div class="abs" role="img" aria-label="Technician repairing commercial kitchen equipment" style="inset:0"></div>
  <div class="hero-shade"></div>
  <svg class="hero-arrow" style="left:90px" width="20" height="30" viewBox="0 0 20 30"><path d="M15 3 4 15l11 12" stroke="#fff" stroke-width="4" fill="none"/></svg>
  <svg class="hero-arrow" style="left:1090px" width="20" height="30" viewBox="0 0 20 30"><path d="m5 3 11 12L5 27" stroke="#fff" stroke-width="4" fill="none"/></svg>
  <h1>KEEPING YOUR KITCHEN COOKING</h1>
  <p>Reliable service and repair for commercial cooking equipment, trusted by<br>restaurants and kitchens across the region.</p>
  <div class="hero-btn">Request Service</div>
</section>

<div class="section-title" style="top:755px"><h2>OUR SERVICES</h2><p>Expert Service for Every Piece of Cooking Equipment</p></div>

<div class="service-card" role="img" aria-label="Commercial kitchen cooking line" style="left:111px;background:linear-gradient(160deg,#9aa0a4,#4b5054)"></div>
<div class="service-card" role="img" aria-label="Technician performing maintenance" style="left:359px;background:linear-gradient(160deg,#6b8fb5,#1f3f7a)"></div>
<div class="service-card" role="img" aria-label="Technician installing an oven" style="left:606px;background:linear-gradient(160deg,#d8d8d8,#3a3a3a)"></div>
<div class="service-card" role="img" aria-label="Oven fire emergency" style="left:853px;background:linear-gradient(160deg,#f7a64a,#b83a0c 60%,#3b1a0c)"></div>
<div class="service-label" style="left:134px">Cooking Equipment<br>Repair</div>
<div class="service-label active" style="left:382px">Preventive<br>Maintenance</div>
<div class="service-label" style="left:629px">Installation &amp; Setup</div>
<div class="service-label" style="left:876px">Emergency Services</div>

<section class="about">
  <svg class="abs" style="left:0;top:0" width="620" height="581" viewBox="0 0 620 581">
    <path d="M0 0H570C650 160 630 420 500 581H0Z" fill="#0a93b6"/>
    <path d="M0 0H485C615 170 610 420 490 581H0Z" fill="#8e9599"/>
  </svg>
  <div class="abs" role="img" aria-label="Stainless steel commercial kitchen" style="left:0;top:0;width:620px;height:581px;clip-path:path('M0 0H485C615 170 610 420 490 581H0Z');background:linear-gradient(150deg,#b7bcbf,#6d7377 55%,#c9cdcf)"></div>
  <div class="about-text">
    <h2>ABOUT US</h2>
    <div class="tag">Your Partner in the Kitchen</div>
    <p class="body">At Junction, we specialize in servicing commercial cooking equipment for restaurants, hotels, and institutional kitchens. Our mission is simple: to keep your kitchen equipment operating at peak performance so you can focus on serving your customers.</p>
    <p class="body">With years of hands-on experience and a reputation for reliability, our team is committed to fast response times, technical excellence, and unmatched customer support.</p>
  </div>
  <div class="outline-btn" style="left:663px;top:471px">Read More</div>
</section>

<div class="section-title" style="top:1928px"><h2>TESTIMONIALS</h2><p>Expert Service for Every Piece of Cooking Equipment</p></div>

<div class="review" style="left:111px">
  <p>Sed ut perspiciatis unde omnis iste natus error sit voluptatem accusantium doloremque laudantium, totam rem aperiam, eaque ipsa quae ab illo inventore veritatis et quasi architecto beatae vitae dicta sunt explicabo. Nemo enim ipsam voluptatem quia voluptas sit aspernatur aut odit aut fugit.</p>
  <div class="reviewer"><div class="avatar" role="img" aria-label="Customer portrait"></div><div><h4>JHONE DEO</h4><div class="stars">★★★★★</div></div></div>
</div>
<div class="review" style="left:440px">
  <p>Sed ut perspiciatis unde omnis iste natus error sit voluptatem accusantium doloremque laudantium, totam rem aperiam, eaque ipsa quae ab illo inventore veritatis et quasi architecto beatae vitae dicta sunt explicabo. Nemo enim ipsam voluptatem quia voluptas sit aspernatur aut odit aut fugit.</p>
  <div class="reviewer"><div class="avatar" role="img" aria-label="Customer portrait"></div><div><h4>JHONE DEO</h4><div class="stars">★★★★★</div></div></div>
</div>
<div class="review" style="left:769px">
  <p>Sed ut perspiciatis unde omnis iste natus error sit voluptatem accusantium doloremque laudantium, totam rem aperiam, eaque ipsa quae ab illo inventore veritatis et quasi architecto beatae vitae dicta sunt explicabo. Nemo enim ipsam voluptatem quia voluptas sit aspernatur aut odit aut fugit.</p>
  <div class="reviewer"><div class="avatar" role="img" aria-label="Customer portrait"></div><div><h4>JHONE DEO</h4><div class="stars">★★★★★</div></div></div>
</div>

<section class="contact" role="img" aria-label="Teal-tinted commercial kitchen backdrop">
  <div class="section-title light" style="top:80px"><h2>CONTACT US</h2><p>Expert Service for Every Piece of Cooking Equipment</p></div>
  <div class="field" style="left:158px;top:205px;width:429px;height:56px">Name</div>
  <div class="field" style="left:612px;top:205px;width:430px;height:56px">Email</div>
  <div class="field" style="left:158px;top:277px;width:429px;height:56px">Phone Number</div>
  <div class="field" style="left:612px;top:277px;width:430px;height:56px">Choose a subject</div>
  <div class="field" style="left:158px;top:350px;width:882px;height:210px">Message</div>
  <div class="outline-btn" style="left:502px;top:603px">Send Now</div>
</section>

<footer class="site-footer">
  <div class="footer-brand"><span class="brand-square"></span>JUNCTION</div>
  <div class="footer-col abs" style="left:512px;top:82px">
    <h3>QUICK LINKS</h3>
    <ul><li>Home</li><li>About Us</li><li>Our Service</li><li>Why Choose Us</li><li>Contact</li></ul>
  </div>
  <div class="footer-col abs" style="left:781px;top:82px;width:300px">
    <h3>GET IN TOUCH</h3>
    <div class="contact-line" style="margin-top:38px">
      <svg width="14" height="18" viewBox="0 0 14 18"><path d="M7 0a7 7 0 0 1 7 7c0 5-7 11-7 11S0 12 0 7a7 7 0 0 1 7-7z" fill="#0a93b6"/><circle cx="7" cy="7" r="2.5" fill="#0b0b0b"/></svg>
      <span>3456 ipsum dolor sit amet, consect etur adipiscing 456</span>
    </div>
    <div class="contact-line" style="margin-top:30px">
      <svg width="16" height="16" viewBox="0 0 24 24"><path fill="#0a93b6" d="M6.6 10.8a15 15 0 0 0 6.6 6.6l2.2-2.2c.3-.3.7-.4 1-.2 1.1.4 2.3.6 3.6.6.6 0 1 .4 1 1V20c0 .6-.4 1-1 1A17 17 0 0 1 3 4c0-.6.4-1 1-1h3.5c.6 0 1 .4 1 1 0 1.3.2 2.5.6 3.6.1.3 0 .7-.2 1z"/></svg>
      <span>+1 555-014-2760</span>
    </div>
    <div class="contact-line" style="margin-top:46px">
      <svg width="16" height="14" viewBox="0 0 16 12"><rect width="16" height="12" rx="1" fill="#0a93b6"/><path d="m1 1 7 5 7-5" stroke="#0b0b0b" stroke-width="1.5" fill="none"/></svg>
      <span>info@junctionkitchen.com</span>
    </div>
  </div>
  <div class="footer-rule"></div>
  <div class="copyright">Copyright 2025. Company Name .All Rights Reserved</div>
</footer>

</body>
</html>
```